Logo for Equipment and Auto parts seller
Crestline Supply and Machinery Corporation
Logo for Equipment and Auto parts seller - Automotive
Creative Brief
Simple
Julien Marceau
Operations Manager
Toliso
Julien.Marceau@cslmcorp.net

```html
<!DOCTYPE html>
<html lang="en">
<head>
<meta charset="utf-8">
<title>Crestline Supply and Machinery Corporation – Business Card</title>
<link rel="stylesheet" href="https://fonts.googleapis.com/css2?family=Roboto+Condensed:wght@400;700&display=swap">
<style>
  :root {
    --navy: #2f2b8e;
    --navy-dark: #25217a;
    --green: #6dbf45;
    --white: #ffffff;
    --paper: #f7f7f7;
    --backdrop: #8a8a8a;
  }
  * { box-sizing: border-box; margin: 0; padding: 0; }
  html, body {
    width: 1200px; height: 908px; overflow: hidden;
    background: var(--backdrop);
    font-family: "Roboto Condensed", "Arial Narrow", sans-serif;
  }
  .stage {
    width: 1200px; height: 908px;
    display: flex; flex-direction: column;
    align-items: center; justify-content: center; gap: 36px;
  }
  .card {
    position: relative; width: 700px; height: 400px;
    border-radius: 22px; overflow: hidden;
  }
  .card--back {
    background: var(--navy);
    display: flex; align-items: center; justify-content: center;
  }
  .card--front { background: var(--paper); }
  .card__wave { position: absolute; inset: 0; width: 100%; height: 100%; }

  .brand { display: flex; flex-direction: column; align-items: center; gap: 14px; }
  .brand__mark {
    width: 64px; height: 64px; border-radius: 50%;
    background: var(--green);
  }
  .brand__name {
    font-weight: 700; font-size: 22px; letter-spacing: 0.5px;
    text-transform: uppercase; text-align: center; line-height: 1.2;
  }
  .card--back .brand__name { color: var(--white); }
  .brand__rule { width: 250px; height: 2px; background: var(--green); }

  .card--front .brand {
    position: absolute; left: 40px; top: 110px; width: 260px;
  }
  .card--front .brand__name { color: var(--navy); font-size: 19px; }
  .card--front .brand__rule { width: 200px; }

  .person {
    position: absolute; right: 40px; top: 40px; text-align: right;
  }
  .person__name { color: var(--navy); font-size: 30px; font-weight: 700; line-height: 1.15; }
  .person__title { color: var(--green); font-size: 20px; margin-top: 2px; line-height: 1.2; }

  .contact {
    position: absolute; right: 40px; top: 222px;
    list-style: none; color: var(--white); font-size: 17px;
    display: flex; flex-direction: column; gap: 12px; align-items: flex-end;
  }
  .contact__item { display: flex; align-items: center; gap: 10px; }
  .contact__icon { width: 20px; height: 20px; flex: none; }
</style>
</head>
<body>
<main class="stage">
  <section class="card card--back" aria-label="Card back">
    <div class="brand">
      <span class="brand__mark" aria-hidden="true"></span>
      <span class="brand__name">Crestline Supply and Machinery Corporation</span>
      <span class="brand__rule" aria-hidden="true"></span>
    </div>
  </section>

  <section class="card card--front" aria-label="Card front">
    <svg class="card__wave" viewBox="0 0 700 400" preserveAspectRatio="none" aria-hidden="true">
      <path fill="var(--green)" d="M0,318 C250,322 390,262 480,196 C560,140 620,132 700,128 L700,150 C620,154 570,162 492,224 C400,298 260,356 0,356Z"/>
      <path fill="var(--navy)" d="M0,360 C262,360 404,302 496,230 C574,168 624,158 700,154 L700,400 L0,400Z"/>
    </svg>

    <div class="brand">
      <span class="brand__mark" aria-hidden="true"></span>
      <span class="brand__name">Crestline Supply and Machinery Corporation</span>
      <span class="brand__rule" aria-hidden="true"></span>
    </div>

    <div class="person">
      <h1 class="person__name">Julien Marceau</h1>
      <p class="person__title">Operations Manager</p>
    </div>

    <ul class="contact">
      <li class="contact__item">Toliso
        <svg class="contact__icon" viewBox="0 0 20 20" aria-hidden="true"><path fill="var(--white)" d="M10 1a6 6 0 0 0-6 6c0 4.5 6 12 6 12s6-7.5 6-12a6 6 0 0 0-6-6zm0 8.5A2.5 2.5 0 1 1 10 4.5a2.5 2.5 0 0 1 0 5z"/></svg>
      </li>
      <li class="contact__item">+225 01 36 58 24
        <svg class="contact__icon" viewBox="0 0 20 20" aria-hidden="true"><path fill="var(--white)" d="M5.5 2l3 3.5-1.8 1.8a11 11 0 0 0 6 6l1.8-1.8L18 14.5l-2 3c-7 0-14-7-14-14z"/></svg>
      </li>
      <li class="contact__item">Julien.Marceau@cslmcorp.net
        <svg class="contact__icon" viewBox="0 0 20 20" aria-hidden="true"><rect x="2" y="4.5" width="16" height="11" rx="1.5" fill="none" stroke="var(--white)" stroke-width="1.6"/><path d="M2.5 5.5l7.5 6 7.5-6" fill="none" stroke="var(--white)" stroke-width="1.6"/></svg>
      </li>
    </ul>
  </section>
</main>
</body>
</html>
```